Flyer Advertisement Design for exotic rental company

Design an advertisement for a exotic rental company:

https://zumacruise.com/

Here is a similar business:

https://www.velvetlanemotors.com/

I rent out a vehicle called a Korvex Tailwind. Here is a link to the manufacturer website:

https://tailwind.korvex.com/en-us/

I have the 2018 Korvex Tailwind GT in the colors Navy Blue and Sunset Red

This advertisement will be printed on a flyer and placed in strategic locations to attract customers. I am looking for something that will draw the customer in. Please use your imagination and come up with something awesome!

Target Market(s)

Outgoing individuals looking to have some fun! This advertisement will be placed in a country club

Industry/Entity Type

Rental Car

Font styles to use
Serif
Sans Serif
Decorative
Script

Colors

Designer to choose colors to be used in the design.

Requirements
Must have
• Pictures of the Korvex Tailwind, website info, message about discount to Maplebrook Country Club Members, phone number, anything else you feel will make the advertisement look great
Nice to have
• Anything you suggest in your professional capacity
Should not have
• Anything goes!

```html
<!DOCTYPE html>
<html lang="en">
<head>
<meta charset="utf-8">
<title>Rent Me – Zuma Cruise Flyer</title>
<link rel="stylesheet" href="https://fonts.googleapis.com/css2?family=Russo+One&family=Montserrat:ital,wght@1,500;1,600;1,700;1,800&display=swap">
<style>
  :root {
    --page-bg: #d4d4d4;
    --flyer-black: #03060d;
    --navy-deep: #050b22;
    --royal-blue: #1658c8;
    --bright-blue: #2b7be6;
    --silver-light: #f4f5f7;
    --silver-mid: #a9adb5;
    --silver-dark: #5d626b;
    --white: #ffffff;
  }
  html, body {
    margin: 0;
    width: 1200px;
    height: 900px;
    overflow: hidden;
    background: var(--page-bg);
  }
  .flyer {
    position: absolute;
    left: 316px;
    top: 74px;
    width: 570px;
    height: 737px;
    overflow: hidden;
    background: radial-gradient(ellipse at 50% 80%, #0c1c4a 0%, var(--navy-deep) 45%, var(--flyer-black) 80%);
    font-family: "Montserrat", sans-serif;
    color: var(--white);
  }
  .flyer-art {
    position: absolute;
    inset: 0;
  }
  .chrome-text {
    background: linear-gradient(180deg, var(--silver-light) 0%, var(--silver-mid) 48%, var(--silver-dark) 52%, var(--silver-light) 100%);
    -webkit-background-clip: text;
    background-clip: text;
    color: transparent;
    filter: drop-shadow(2px 2px 0 #0d2e7a) drop-shadow(0 0 2px #000);
  }
  .headline {
    position: absolute;
    top: 34px;
    left: 0;
    width: 100%;
    margin: 0;
    text-align: center;
    font-family: "Russo One", sans-serif;
    font-weight: 400;
    font-size: 92px;
    line-height: 1;
    letter-spacing: -3px;
    transform: scaleX(1.32) skewX(-16deg);
  }
  .site-band {
    position: absolute;
    top: 131px;
    left: 36px;
    width: 504px;
    height: 24px;
    background: linear-gradient(90deg, rgba(22,88,200,0) 0%, var(--royal-blue) 12%, var(--royal-blue) 88%, rgba(22,88,200,0) 100%);
    text-align: center;
    font-style: italic;
    font-weight: 500;
    font-size: 22px;
    line-height: 24px;
    letter-spacing: 12px;
  }
  .phone {
    position: absolute;
    top: 438px;
    left: 0;
    width: 100%;
    margin: 0;
    text-align: center;
    font-family: "Russo One", sans-serif;
    font-size: 60px;
    line-height: 1;
    letter-spacing: -2px;
    transform: scaleX(1.3) skewX(-16deg);
  }
  .offer {
    position: absolute;
    top: 510px;
    left: 0;
    width: 100%;
    margin: 0;
    text-align: center;
    font-style: italic;
    font-weight: 500;
    font-size: 21px;
    line-height: 28px;
  }
  .offer strong { font-weight: 800; }
  .signup-band {
    position: absolute;
    top: 608px;
    left: 40px;
    width: 500px;
    height: 44px;
    background: linear-gradient(90deg, rgba(22,88,200,0) 0%, var(--royal-blue) 22%, var(--bright-blue) 50%, var(--royal-blue) 78%, rgba(22,88,200,0) 100%);
    text-align: center;
    font-family: "Russo One", sans-serif;
    font-size: 40px;
    line-height: 44px;
    letter-spacing: -2px;
  }
  .signup-band span {
    display: inline-block;
    transform: scaleX(1.3) skewX(-16deg);
    text-shadow: 1px 1px 0 #0a2a6e;
  }
  .signup-url {
    position: absolute;
    top: 659px;
    left: 0;
    width: 100%;
    margin: 0;
    text-align: center;
    font-style: italic;
    font-weight: 600;
    font-size: 21px;
  }
</style>
</head>
<body>
  <main class="flyer">
    <svg class="flyer-art" width="570" height="737" viewBox="0 0 570 737">
      <defs>
        <linearGradient id="garage-tone" x1="0" y1="0" x2="0" y2="1">
          <stop offset="0" stop-color="#4a5252"/>
          <stop offset="0.45" stop-color="#343c3e"/>
          <stop offset="1" stop-color="#181d24"/>
        </linearGradient>
        <linearGradient id="stripe-blue" x1="0" y1="0" x2="1" y2="0">
          <stop offset="0" stop-color="#1a5fd0"/>
          <stop offset="1" stop-color="#2a86ee"/>
        </linearGradient>
        <radialGradient id="vehicle-tone" cx="0.45" cy="0.55" r="0.6">
          <stop offset="0" stop-color="#2a3f8e"/>
          <stop offset="0.6" stop-color="#16245c"/>
          <stop offset="1" stop-color="#0a1030"/>
        </radialGradient>
      </defs>
      <polygon class="photo-area" role="img"
        aria-label="Lit underground parking garage with concrete pillars"
        points="0,0 570,0 570,430 0,272" fill="url(#garage-tone)"/>
      <polygon class="accent-stripe" points="0,266 570,422 570,498 0,342" fill="url(#stripe-blue)"/>
      <polygon class="accent-stripe-dark" points="0,300 570,456 570,468 0,312" fill="#0f3f9a" opacity="0.7"/>
      <polygon class="accent-stripe-light" points="0,326 570,482 570,488 0,332" fill="#5aa4ff" opacity="0.6"/>
      <rect class="vehicle-photo" role="img"
        aria-label="Navy blue Korvex Tailwind GT three-wheeler, front three-quarter view"
        x="74" y="168" width="440" height="250" rx="60" fill="url(#vehicle-tone)"/>
    </svg>

    <h1 class="headline chrome-text">RENT ME</h1>
    <div class="site-band">WWW.ZUMACRUISE.COM</div>

    <p class="phone chrome-text">555 214 7730</p>

    <p class="offer"><strong>20%</strong> Off for all Maplebrook Country<br>Club Members</p>

    <div class="signup-band"><span>SIGN UP AT</span></div>
    <p class="signup-url">www.zumacruise.com/MaplebrookCC</p>
  </main>
</body>
</html>
```